K7 Electrical Services Ltd Web design

I require a web site for my new electrical contracting company. We are customer service orientated. Offering high value electrical installations, design and maintenance. Focused on custom residential and commercial upgrading. Lighting design and application are paramount in our company's services. Industry leading product use and integration are always on the forefront with our customer client services. As well as energy efficiency.

Target Market(s)

Homebuilders, General Contractors, Property management companies, clients, individuals,

Industry/Entity Type

Electric Company

Coding

Coded - Design and coding required

Number of Pages Required

3 page

Requirements
Must have
• Classic, modern, edgy but not trendy . Appeals to the masse.
• 3 page
• home page
• about page
• gallery page
• ability to contact from the webiste
Nice to have
• open to all types of designs that are relative to the construction industry.
• Black, Grey, metallic ice blue and deep purple colours from the logo.
Should not have
• anything cheesy with cartoon light bulb images.

```html
<!DOCTYPE html>
<html lang="en">
<head>
<meta charset="utf-8">
<title>K7 Electrical Services Ltd</title>
<link href="https://fonts.googleapis.com/css2?family=Roboto:wght@400;500;700&family=Roboto+Condensed:wght@400;700&family=Oswald:wght@400;500&display=swap" rel="stylesheet">
<style>
:root{
  --purple:#6a2c98;
  --purple-dark:#4d1d74;
  --ink:#222226;
  --text:#555;
  --muted:#777;
  --light:#f2f2f3;
  --line:#dcdcdc;
  --white:#fff;
}
*{margin:0;padding:0;box-sizing:border-box}
html,body{width:1200px;height:3523px;overflow:hidden}
body{position:relative;background:var(--white);font-family:Roboto,Arial,sans-serif;color:var(--text)}
.abs{position:absolute}
.display{font-family:Oswald,"Arial Narrow",sans-serif}

/* wordmark: one colour, one weight, one plain square */
.wordmark{position:absolute;display:flex;align-items:center;gap:10px;font-family:Roboto,Arial,sans-serif;font-weight:500;color:var(--purple);white-space:nowrap}
.wordmark::before{content:"";width:14px;height:14px;background:var(--purple);flex:none}

/* header */
.site-header{position:absolute;left:0;top:0;width:1200px;height:122px;background:var(--white)}
.site-header .wordmark{left:99px;top:44px;font-size:22px}
.header-phone{position:absolute;left:606px;top:30px;font-size:20px;color:#444;display:flex;align-items:center;gap:8px}
.estimate-btn{position:absolute;left:871px;top:21px;width:228px;height:38px;background:var(--purple);color:#fff;font-family:"Roboto Condensed",sans-serif;font-weight:700;font-size:16px;display:flex;align-items:center;justify-content:center;border-radius:3px}
.main-nav{position:absolute;right:101px;top:78px;display:flex;gap:30px;font-size:17px;font-weight:500;color:#333}

/* hero */
.hero{position:absolute;left:0;top:122px;width:1200px;height:575px;background:radial-gradient(ellipse at 68% 18%,#c8d4ff 0%,#5a6ab0 10%,#27304e 32%,#141826 62%,#0b0d14 100%)}
.hero-kicker{position:absolute;left:99px;top:182px;font-size:33px;line-height:40px;color:#fff;font-weight:400}
.hero-title{position:absolute;left:99px;top:222px;font-size:52px;line-height:62px;color:#fff;font-weight:500}
.hero-btn{position:absolute;left:99px;top:306px;width:127px;height:38px;border:2px solid #fff;color:#fff;font-size:14px;display:flex;align-items:center;justify-content:center}
.hero-dots{position:absolute;left:99px;top:372px;display:flex;gap:12px}
.hero-dots i{width:13px;height:13px;border-radius:50%;background:rgba(255,255,255,.6)}
.hero-dots i:first-child{background:#fff}

/* welcome */
.welcome-photo{position:absolute;left:99px;top:784px;width:481px;height:362px;background:linear-gradient(135deg,#dfe7f0,#7d93b2 55%,#3b4e70);border:1px solid var(--line)}
.welcome{position:absolute;left:620px;top:790px;width:480px}
.welcome h2{font-family:"Roboto Condensed",sans-serif;font-size:31px;color:var(--ink);font-weight:700}
.welcome p{margin-top:18px;font-size:12.5px;line-height:21px;color:var(--muted)}
.check-list{list-style:none;margin-top:18px}
.check-list li{font-size:13.5px;color:#444;height:31px;display:flex;align-items:center;gap:14px}
.check-list svg{flex:none}
.btn{background:var(--purple);color:#fff;font-family:"Roboto Condensed",sans-serif;font-weight:700;font-size:15px;display:flex;align-items:center;justify-content:center;border-radius:3px}
.welcome .btn{margin-top:14px;width:141px;height:36px}

/* sectors */
.sectors{position:absolute;left:0;top:1252px;width:1200px;height:429px;overflow:hidden;background:#0f1424}
.sector{position:absolute;top:0;height:429px}
.sector-label{position:absolute;top:196px;font-family:Oswald,"Arial Narrow",sans-serif;font-weight:500;font-size:27px;color:#fff;transform:translateX(-50%);white-space:nowrap}

/* services */
.section-title{position:absolute;left:0;width:1200px;text-align:center;font-family:"Roboto Condensed",sans-serif;font-weight:700;font-size:36px;color:var(--ink)}
.divider{position:absolute;left:520px;width:160px;height:20px}
.service{position:absolute;width:500px;height:150px}
.service .icon{position:absolute;left:0;top:0;width:103px;height:103px;border-radius:50%;border:3px solid var(--purple);display:flex;align-items:center;justify-content:center}
.service .icon span{width:86px;height:86px;border-radius:50%;background:var(--purple);display:flex;align-items:center;justify-content:center}
.service h3{position:absolute;left:128px;top:2px;font-size:19px;font-weight:500;color:var(--ink)}
.service p{position:absolute;left:128px;top:36px;width:360px;font-size:12.5px;line-height:22px;color:var(--muted)}

/* testimonial */
.testimonial{position:absolute;left:0;top:2301px;width:1200px;height:317px;background:linear-gradient(90deg,#5b5b66 0%,#5d4a78 45%,#6d3aa0 75%,#7a3fb0 100%)}
.quote-mark{position:absolute;left:0;width:1200px;top:42px;text-align:center;font-family:Georgia,serif;font-size:110px;line-height:1;color:#fff;height:70px;overflow:hidden}
.quote-text{position:absolute;left:230px;width:740px;top:117px;text-align:center;color:#fff;font-size:14px;line-height:26px}
.quote-name{position:absolute;left:0;width:1200px;top:210px;text-align:center;color:#fff;font-size:14px;font-style:italic;font-weight:500}
.t-dots{position:absolute;left:570px;top:258px;display:flex;gap:8px}
.t-dots i{width:18px;height:3px;background:rgba(255,255,255,.5)}
.t-dots i:first-child{background:#fff}

/* blog */
.post{position:absolute;top:2794px;width:312px}
.post-photo{width:312px;height:183px;position:relative}
.date-badge{position:absolute;right:6px;top:0;width:44px;height:70px;background:var(--purple);color:#fff;font-size:13px;line-height:18px;text-align:center;padding-top:7px;font-weight:500}
.post h4{margin-top:22px;font-size:17px;font-weight:500;color:var(--ink)}
.post p{margin-top:10px;font-size:12.5px;line-height:20px;color:var(--muted)}

/* footer */
.site-footer{position:absolute;left:0;top:3170px;width:1200px;height:305px;background:var(--light)}
.site-footer .wordmark{left:99px;top:106px;font-size:15px;gap:7px}
.site-footer .wordmark::before{width:10px;height:10px}
.socials{position:absolute;left:131px;top:154px;display:flex;gap:7px}
.socials i{width:26px;height:26px;border-radius:50%;border:2px solid var(--purple)}
.footer-col h5{font-family:"Roboto Condensed",sans-serif;font-size:21px;font-weight:700;color:var(--ink)}
.contact-list{list-style:none;margin-top:22px}
.contact-list li{display:flex;gap:12px;font-size:13px;line-height:20px;color:#444;margin-bottom:14px}
.newsletter p{margin-top:20px;font-size:12px;line-height:19px;color:var(--muted);width:280px}
.email-field{margin-top:14px;width:280px;height:40px;background:#fff;border:1px solid var(--line);font-size:12px;color:#999;padding:12px}
.newsletter .btn{margin-top:14px;width:122px;height:40px;font-size:14px}
.quick-links{list-style:none;margin-top:16px}
.quick-links li{font-size:13px;color:#444;height:26px;display:flex;align-items:center;gap:10px}
.quick-links li::before{content:"";border-left:6px solid var(--ink);border-top:4px solid transparent;border-bottom:4px solid transparent}
.copyright{position:absolute;left:0;top:3475px;width:1200px;height:48px;background:var(--white);text-align:center;font-size:13px;line-height:48px;color:#555;border-top:1px solid var(--line)}
</style>
</head>
<body>

<header class="site-header">
  <div class="wordmark">K7 Electrical Services Ltd</div>
  <div class="header-phone">
    <svg width="20" height="20" viewBox="0 0 24 24"><path fill="#555" d="M6.6 10.8a15 15 0 0 0 6.6 6.6l2.2-2.2c.3-.3.7-.4 1-.2 1.1.4 2.3.6 3.6.6.6 0 1 .4 1 1V20c0 .6-.4 1-1 1A17 17 0 0 1 3 4c0-.6.4-1 1-1h3.5c.6 0 1 .4 1 1 0 1.3.2 2.5.6 3.6.1.3 0 .7-.2 1z"/></svg>
    Call Us : 800 555 0147
  </div>
  <div class="estimate-btn">REQUEST A FREE ESTIMATE</div>
  <nav class="main-nav"><span>HOME</span><span>ABOUT US</span><span>OUR SERVICES</span><span>PROJECTS</span><span>BLOG</span><span>CONTACT US</span></nav>
</header>

<section class="hero" role="img" aria-label="Electrician in a hard hat holding a sparking cable above a night city skyline">
  <div class="hero-kicker display">FAST ELECTRICIAN SERVICES</div>
  <div class="hero-title display">BENEFITS OF ELECTRICIAN</div>
  <div class="hero-btn">READ MORE</div>
  <div class="hero-dots"><i></i><i></i><i></i></div>
</section>

<div class="welcome-photo" role="img" aria-label="Electrician in a blue cap working on a switchboard"></div>
<section class="welcome">
  <h2>WELCOME TO &nbsp;K7 ELECTRICAL</h2>
  <p>Sed ut perspiciatis unde omnis iste natus error sit voluptatem accusantium loremque laudantium, totam rem aperiam, eaque ipsa quae ab illo inventore veritatis et quasi architecto beatae vitae dicta sunt explicabo. Nemo enim ipsam voluptatem quia voluptas sit aspernatur aut odit aut fugit, sed quia consequuntur</p>
  <ul class="check-list">
    <li><svg width="10" height="10" viewBox="0 0 10 10"><circle cx="5" cy="5" r="5" fill="#6a2c98"/><path d="M4 3l2 2-2 2" stroke="#fff" stroke-width="1.3" fill="none"/></svg>Full-service electrical</li>
    <li><svg width="10" height="10" viewBox="0 0 10 10"><circle cx="5" cy="5" r="5" fill="#6a2c98"/><path d="M4 3l2 2-2 2" stroke="#fff" stroke-width="1.3" fill="none"/></svg>Wiring and installation/upgrades</li>
    <li><svg width="10" height="10" viewBox="0 0 10 10"><circle cx="5" cy="5" r="5" fill="#6a2c98"/><path d="M4 3l2 2-2 2" stroke="#fff" stroke-width="1.3" fill="none"/></svg>Emergency power solutions (generators)</li>
    <li><svg width="10" height="10" viewBox="0 0 10 10"><circle cx="5" cy="5" r="5" fill="#6a2c98"/><path d="M4 3l2 2-2 2" stroke="#fff" stroke-width="1.3" fill="none"/></svg>Virtually any electrical needs you have – just ask!</li>
  </ul>
  <div class="btn">READ MORE</div>
</section>

<section class="sectors">
  <div class="sector" style="left:0;width:470px;background:linear-gradient(160deg,#2a2f3c,#6b5140 55%,#3a2a20);clip-path:polygon(0 0,100% 0,415px 100%,0 100%)" role="img" aria-label="Warm residential living room interior"></div>
  <div class="sector" style="left:425px;width:370px;background:linear-gradient(160deg,#3d4658,#8a99ae 50%,#2f3a4e);clip-path:polygon(45px 0,100% 0,320px 100%,0 100%)" role="img" aria-label="Electrician working on commercial wiring"></div>
  <div class="sector" style="left:755px;width:445px;background:linear-gradient(160deg,#1d2233,#7a6240 45%,#3c2c1e);clip-path:polygon(40px 0,100% 0,100% 100%,0 100%)" role="img" aria-label="Pendant lights over a dining area"></div>
  <svg class="abs" style="left:0;top:0" width="1200" height="429"><path d="M470 0L417 429M797 0L752 429" stroke="#fff" stroke-width="4"/></svg>
  <div class="sector-label" style="left:277px">RESIDENTIAL</div>
  <div class="sector-label" style="left:601px">COMMERCIAL</div>
  <div class="sector-label" style="left:923px">LIGHTING DESIGN</div>
</section>

<h2 class="section-title" style="top:1756px">K7 ELECTRICAL SERVICES</h2>
<svg class="divider" style="top:1822px" viewBox="0 0 160 20"><path d="M0 10H66M94 10H160" stroke="#6a2c98" stroke-width="2"/><path d="M83 1L73 11h7l-4 8 11-11h-7z" fill="#6a2c98"/></svg>

<div class="service" style="left:104px;top:1895px">
  <div class="icon"><span><svg width="44" height="44" viewBox="0 0 44 44" fill="none" stroke="#fff" stroke-width="3"><circle cx="22" cy="22" r="15"/><path d="M17 14v6M27 14v6M14 20h16v4a8 8 0 0 1-16 0zM22 32v8"/></svg></span></div>
  <h3>Electrical Installations</h3>
  <p>Sed ut perspiciatis unde omnis iste natus error sit voluptatem accusantium doloremque laudantium, totam rem aperiam, eaque ipsa quae ab illo inventore veritatis et quasi architecto beatae vitae dicta sunt explicabo.</p>
</div>
<div class="service" style="left:640px;top:1895px">
  <div class="icon"><span><svg width="44" height="44" viewBox="0 0 44 44" fill="none" stroke="#fff" stroke-width="3"><rect x="10" y="6" width="24" height="32"/><path d="M16 14h12M16 21h12M16 28h7"/></svg></span></div>
  <h3>Electrical Design</h3>
  <p>Sed ut perspiciatis unde omnis iste natus error sit voluptatem accusantium doloremque laudantium, totam rem aperiam, eaque ipsa quae ab illo inventore veritatis et quasi architecto beatae vitae dicta sunt explicabo.</p>
</div>
<div class="service" style="left:104px;top:2072px">
  <div class="icon"><span><svg width="44" height="44" viewBox="0 0 44 44" fill="none" stroke="#fff" stroke-width="3.5" stroke-linecap="round"><path d="M10 34L30 14M30 8a6 6 0 1 0 6 6M34 34L14 14M10 10l4 4"/></svg></span></div>
  <h3>Maintenance</h3>
  <p>Sed ut perspiciatis unde omnis iste natus error sit voluptatem accusantium doloremque laudantium, totam rem aperiam, eaque ipsa quae ab illo inventore veritatis et quasi architecto beatae vitae dicta sunt explicabo.</p>
</div>
<div class="service" style="left:640px;top:2072px">
  <div class="icon"><span><svg width="44" height="44" viewBox="0 0 44 44" fill="none" stroke="#fff" stroke-width="3"><circle cx="22" cy="22" r="8"/><path d="M22 6v6M22 32v6M6 22h6M32 22h6M11 11l4 4M29 29l4 4M33 11l-4 4M11 33l4-4"/></svg></span></div>
  <h3>Electrical Contracting</h3>
  <p>Sed ut perspiciatis unde omnis iste natus error sit voluptatem accusantium doloremque laudantium, totam rem aperiam, eaque ipsa quae ab illo inventore veritatis et quasi architecto beatae vitae dicta sunt explicabo.</p>
</div>

<section class="testimonial" role="img" aria-label="Switchboard wiring behind a purple tint">
  <svg class="abs" style="left:0;top:0" width="1200" height="317" fill="none" stroke="#fff" stroke-width="3"><path d="M197 110V64H262M1005 200V247H940"/></svg>
  <div class="quote-mark">&#8221;</div>
  <p class="quote-text">Sed ut perspiciatis unde omnis iste natus error sit voluptatem accusantium doloremque laudantium, totam rem aperiam, eaque ipsa quae ab illo inventore veritatis et quasi architecto beatae vitae dicta sunt explicabo. Nemo enim ipsam voluptatem quia voluptas sit aspernatur aut odit aut fugit, sed quia consequuntur .</p>
  <div class="quote-name">Sam Carter - K7 Electrical</div>
  <div class="t-dots"><i></i><i></i><i></i></div>
</section>

<h2 class="section-title" style="top:2678px">LATEST BLOG</h2>
<svg class="divider" style="top:2732px" viewBox="0 0 160 20"><path d="M0 10H66M94 10H160" stroke="#6a2c98" stroke-width="2"/><path d="M83 1L73 11h7l-4 8 11-11h-7z" fill="#6a2c98"/></svg>

<article class="post" style="left:99px">
  <div class="post-photo" role="img" aria-label="Multimeter testing wires in a panel" style="background:linear-gradient(135deg,#c83a2e,#e0b23a 45%,#4a3a38)"><div class="date-badge">SEP<br>09<br>2018</div></div>
  <h4>Nemo enim ipsam voluptatem quia</h4>
  <p>Sed ut perspiciatis unde omnis iste natus error sit atem accusantium doloremque laudantium, totam rem apm, eaque ipsa quae ab illo inventore veritatis</p>
</article>
<article class="post" style="left:446px">
  <div class="post-photo" role="img" aria-label="Electrician in a yellow hard hat at a fuse board" style="background:linear-gradient(135deg,#e8e4d8,#c9a73a 40%,#6d6a60)"><div class="date-badge">SEP<br>09<br>2018</div></div>
  <h4>Nemo enim ipsam voluptatem quia</h4>
  <p>Sed ut perspiciatis unde omnis iste natus error sit atem accusantium doloremque laudantium, totam rem apm, eaque ipsa quae ab illo inventore veritatis</p>
</article>
<article class="post" style="left:789px">
  <div class="post-photo" role="img" aria-label="Technician connecting wires against a white wall" style="background:linear-gradient(135deg,#f4f4f4,#d7d3cf 55%,#5a4a42)"><div class="date-badge">SEP<br>09<br>2018</div></div>
  <h4>Nemo enim ipsam voluptatem quia</h4>
  <p>Sed ut perspiciatis unde omnis iste natus error sit atem accusantium doloremque laudantium, totam rem apm, eaque ipsa quae ab illo inventore veritatis</p>
</article>

<footer class="site-footer">
  <div class="wordmark">K7 Electrical Services Ltd</div>
  <div class="socials"><i></i><i></i><i></i><i></i></div>

  <div class="footer-col abs" style="left:352px;top:57px">
    <h5>CONTACT US</h5>
    <ul class="contact-list">
      <li><svg width="12" height="16" viewBox="0 0 12 16"><path fill="#444" d="M6 0a6 6 0 0 1 6 6c0 4-6 10-6 10S0 10 0 6a6 6 0 0 1 6-6zm0 3.5A2.5 2.5 0 1 0 6 8.5 2.5 2.5 0 0 0 6 3.5z"/></svg><span>K7 Electrical 58 Example Road,<br>Northvale, VIC 3000</span></li>
      <li><svg width="14" height="14" viewBox="0 0 24 24"><path fill="#444" d="M6.6 10.8a15 15 0 0 0 6.6 6.6l2.2-2.2c.3-.3.7-.4 1-.2 1.1.4 2.3.6 3.6.6.6 0 1 .4 1 1V20c0 .6-.4 1-1 1A17 17 0 0 1 3 4c0-.6.4-1 1-1h3.5c.6 0 1 .4 1 1 0 1.3.2 2.5.6 3.6.1.3 0 .7-.2 1z"/></svg><span>Phone: 1-888-555-0193</span></li>
      <li><svg width="14" height="12" viewBox="0 0 14 12"><rect x="0.5" y="0.5" width="13" height="11" fill="none" stroke="#444"/><path d="M1 1l6 5 6-5" fill="none" stroke="#444"/></svg><span>hello@k7electrical.example</span></li>
    </ul>
  </div>

  <div class="footer-col newsletter abs" style="left:646px;top:57px">
    <h5>SIGN UP FOR NEWSLETTER</h5>
    <p>Excepteur sint occaecat cupidatat non proident, sunt in culpa qui officia deserunt</p>
    <div class="email-field">Enter email</div>
    <div class="btn">SUBSCRIPTION</div>
  </div>

  <div class="footer-col abs" style="left:979px;top:57px">
    <h5>QUICK LINKS</h5>
    <ul class="quick-links"><li>Home</li><li>About</li><li>Service</li><li>Projects</li><li>Blog</li><li>Contact</li></ul>
  </div>
</footer>

<div class="copyright">©2018 K7 Electrical. All Rights Reserved.</div>

</body>
</html>
```